Landing Page Design for Cancer Article

We need to have relevant custom graphics and images incorporated with the text of the Google Doc. The Google Doc contains content for an article that informs users about Stomach Cancer. The article was written by a non-profit organization that promotes education and awareness about this disease. Their website address is www.velsantrum.org so you can see their current color theme and branding.

Basically, we're just looking to make the article look more polished. We don't want users coming to the article and just see a wall of text. We'd like graphics and images relevant to the content. Also the layout to make readability easier. Let me know if you have more questions.

https://files.quorbinet.com/document/d/8KpLmWnRtYbVcXzQaSdFgHjKlMnBv/edit?usp=sharing&ouid=493027618450397261845&rtpof=true&sd=true

```html
<!DOCTYPE html>
<html lang="en">
<head>
<meta charset="utf-8">
<title>About Stomach Cancer – Velsantrum Family Foundation</title>
<link href="https://fonts.googleapis.com/css2?family=Questrial&family=Raleway:wght@400;500;600;700&display=swap" rel="stylesheet">
<style>
:root{
  --brand:#0a6ebd;
  --brand-title:#1c6cc0;
  --ink:#2b2b2b;
  --muted:#555;
  --soft:#f4f5f7;
  --panel:#f7f7f8;
  --gold:#f6b90b;
  --heart:#f06a2a;
  --white:#fff;
  --navy:#0b2a63;
}
*{box-sizing:border-box;margin:0;padding:0}
html,body{width:1200px;height:4271px;overflow:hidden}
body{font-family:"Raleway",sans-serif;color:var(--ink);background:var(--white);position:relative}
h1,h2,.brand-name,.stat-value{font-family:"Questrial",sans-serif;font-weight:400}
section,header,footer{position:relative;width:1200px;overflow:hidden}
.abs{position:absolute}

/* header */
.site-header{height:95px}
.brand{left:88px;top:28px;display:flex;align-items:center;gap:10px}
.brand-mark{width:28px;height:28px;border-radius:50%;background:var(--brand)}
.brand-name{color:var(--brand);font-size:17px;line-height:1}
.nav{right:110px;top:30px;display:flex;align-items:center;gap:30px;font-size:13px;font-weight:600}
.nav a{color:#222;text-decoration:none;display:flex;align-items:center;gap:8px}
.donate{background:var(--gold);border-radius:20px;padding:9px 16px;font-weight:700;display:flex;align-items:center;gap:8px;color:#222}

/* hero */
.hero{height:515px}
.hero-panel{left:0;top:0;width:613px;height:515px;background:var(--brand)}
.hero-photo{left:613px;top:0;width:587px;height:515px;background:linear-gradient(160deg,#c9c6c6 0%,#eeeded 45%,#f4d6cf 75%,#f2b4a2 100%)}
.hero h1{left:89px;top:83px;width:430px;color:var(--white);font-size:34px;line-height:41px}
.hero p{left:89px;top:272px;width:460px;color:var(--white);font-size:14px;line-height:20px}

/* causes */
.causes{height:545px}
.section-title{color:var(--brand-title);font-size:30px}
.causes .section-title{top:56px;width:100%;text-align:center}
.causes .lead{top:106px;left:260px;width:680px;text-align:center;font-size:15px;font-weight:600;line-height:20px;color:#222}
.cause-left{left:110px;top:188px;width:465px;font-size:15px;line-height:20px}
.cause-head{display:flex;gap:14px;align-items:flex-start;margin-bottom:10px}
.checks{list-style:none;margin-left:42px}
.checks li{display:flex;gap:8px;margin-bottom:11px;color:#333}
.checks svg{flex:0 0 14px;margin-top:3px}
.cause-right{left:625px;top:188px;width:440px;font-size:15px;line-height:20px;list-style:none}
.cause-right li{display:flex;gap:14px;margin-bottom:22px;color:#333}
.icon{flex:0 0 28px}

/* symptoms */
.symptoms{height:620px}
.diagram{left:85px;top:78px;width:445px;height:390px;border-radius:6px;background:linear-gradient(180deg,#f6e4dc 0%,#f2c6bb 45%,#fbf6f4 60%,#f0bfb5 100%)}
.symptoms .section-title{left:567px;top:54px}
.symptom-card{left:560px;width:530px;background:var(--soft);border-radius:10px;padding:22px 34px;font-size:13.5px;line-height:18px}
.symptom-card h3{font-size:13.5px;font-weight:600;margin-bottom:10px;color:#222}
.symptom-card ul{margin-left:16px;color:#444}
.card-early{top:110px;height:178px}
.card-late{top:297px;height:240px}

/* diagnosis */
.diagnosis{height:667px;background:linear-gradient(100deg,#0b68b5 0%,#0f6bb2 38%,#2b4f8a 60%,#4c7fb5 80%,#1b6fb6 100%)}
.diagnosis-art{right:0;top:0;width:620px;height:667px;background:radial-gradient(circle at 70% 55%,rgba(120,200,240,.55) 0%,rgba(40,90,150,.2) 40%,rgba(10,60,120,0) 70%)}
.diagnosis .section-title{left:76px;top:60px;color:var(--white)}
.diag-lead{left:76px;top:116px;width:550px;font-size:15px;font-weight:600;line-height:20px;color:var(--white)}
.diag-sub{left:78px;top:255px;font-size:14px;font-weight:600;color:var(--white)}
.diag-list{left:76px;top:290px;width:584px;list-style:none;color:var(--white);font-size:13px;line-height:18px}
.diag-list li{display:flex;gap:20px;margin-bottom:30px}
.diag-list svg{flex:0 0 14px;margin-top:2px}
.diag-foot{left:79px;top:605px;font-size:13.5px;font-weight:600;color:var(--white)}

/* treatments */
.treatments{height:753px}
.care-photo{left:73px;top:61px;width:410px;height:592px;background:linear-gradient(135deg,#d9e3e4 0%,#b8cfd3 40%,#5f8fc1 75%,#2c5f9d 100%)}
.treatments .section-title{left:518px;top:64px}
.treat-copy{left:518px;top:120px;width:582px;font-size:13.5px;line-height:21.5px;color:#444}
.treat-copy p{margin-bottom:21px}

/* survival */
.survival{height:608px;background:var(--panel)}
.survival .section-title{left:78px;top:48px}
.surv-copy{left:78px;top:107px;width:580px;font-size:13.5px;line-height:21.5px;color:#444}
.surv-copy p{margin-bottom:21px}
.stat-card{background:var(--white);border-radius:12px;padding:22px 16px 0 16px;box-shadow:0 2px 10px rgba(0,0,0,.04)}
.stat-head{display:flex;gap:10px;font-size:13px;font-weight:600;line-height:16px;color:#222}
.stat-value{color:var(--brand-title);font-size:40px;margin:20px 0 0 36px}
.stat-local{left:706px;top:128px;width:207px;height:190px}
.stat-regional{left:934px;top:220px;width:200px;height:175px}
.stat-distant{left:706px;top:350px;width:207px;height:170px}

/* closing band */
.closing{height:333px;background:radial-gradient(ellipse at 50% 30%,#8a3a20 0%,#3a2c5a 25%,#132f6e 55%,var(--navy) 100%)}
.closing p{left:270px;top:105px;width:660px;text-align:center;color:var(--white);font-size:20px;line-height:29px}

/* footer */
.site-footer{height:145px}
.site-footer .brand{left:100px;top:56px}
.foot-contact{left:410px;top:53px;font-size:12px;font-weight:600;line-height:20px;color:#222}
.foot-contact div{display:flex;gap:10px;align-items:center}
.foot-legal{left:676px;top:50px;width:400px;font-size:11px;line-height:16px;color:#666}
</style>
</head>
<body>

<header class="site-header">
  <div class="brand abs"><span class="brand-mark"></span><span class="brand-name">Velsantrum Family Foundation</span></div>
  <nav class="nav abs">
    <a href="#">Homepage</a>
    <a href="#"><svg width="16" height="12" viewBox="0 0 16 12" fill="none" stroke="#0a6ebd" stroke-width="1.4"><rect x="1" y="1" width="14" height="10" rx="1"/><path d="M1 1l7 6 7-6"/></svg>mara@velsantrum.org</a>
    <a href="#" class="donate">DONATE <svg width="14" height="12" viewBox="0 0 14 12"><path d="M7 12L1.2 6.2A3.4 3.4 0 0 1 7 1.6a3.4 3.4 0 0 1 5.8 4.6z" fill="#f06a2a"/></svg></a>
  </nav>
</header>

<section class="hero">
  <div class="hero-panel abs"></div>
  <div class="hero-photo abs" role="img" aria-label="Woman holding her hand over her abdomen with the stomach and digestive tract highlighted in red"></div>
  <h1 class="abs">About Stomach Cancer: Types, Causes, Symptoms, Treatments, Cures and Research</h1>
  <p class="abs">Let’s go through the different causes and symptoms of stomach cancer. Then, we’ll touch on some of the current ways to diagnose and treat stomach cancer. Finally, we’ll discuss the survival rates and research concerning stomach cancer. This guide is based on information from the National Oncology Bureau (NOB), the U.S. government's principal agency for cancer research.</p>
</section>

<section class="causes">
  <h2 class="section-title abs">Possible Causes of Stomach Cancer</h2>
  <p class="lead abs">Stomach cancer occurs for many reasons. For some people, genetics plays a significant role. Here are some of the biggest risk factors associated with stomach cancer.</p>
  <div class="cause-left abs">
    <div class="cause-head">
      <svg class="icon" width="28" height="24" viewBox="0 0 28 24" fill="none" stroke="#0a6ebd" stroke-width="1.5"><rect x="2" y="5" width="24" height="17" rx="2"/><path d="M10 5V2h8v3M14 9v9M9.5 13.5h9"/></svg>
      <span>Having any of the following medical conditions:</span>
    </div>
    <ul class="checks">
      <li><svg width="14" height="14" viewBox="0 0 14 14" fill="none" stroke="#333" stroke-width="1.3"><circle cx="7" cy="7" r="6"/><path d="M4 7l2 2 4-4"/></svg>Helicobacter pylori (H. pylori) infection of the stomach</li>
      <li><svg width="14" height="14" viewBox="0 0 14 14" fill="none" stroke="#333" stroke-width="1.3"><circle cx="7" cy="7" r="6"/><path d="M4 7l2 2 4-4"/></svg>Chronic gastritis (inflammation of the stomach)</li>
      <li><svg width="14" height="14" viewBox="0 0 14 14" fill="none" stroke="#333" stroke-width="1.3"><circle cx="7" cy="7" r="6"/><path d="M4 7l2 2 4-4"/></svg>Pernicious anemia</li>
      <li><svg width="14" height="14" viewBox="0 0 14 14" fill="none" stroke="#333" stroke-width="1.3"><circle cx="7" cy="7" r="6"/><path d="M4 7l2 2 4-4"/></svg>Intestinal metaplasia (a condition in which the normal stomach lining is replaced with the cells that line the intestines)</li>
      <li><svg width="14" height="14" viewBox="0 0 14 14" fill="none" stroke="#333" stroke-width="1.3"><circle cx="7" cy="7" r="6"/><path d="M4 7l2 2 4-4"/></svg>Gastric polyps</li>
      <li><svg width="14" height="14" viewBox="0 0 14 14" fill="none" stroke="#333" stroke-width="1.3"><circle cx="7" cy="7" r="6"/><path d="M4 7l2 2 4-4"/></svg>Epstein-Barr virus infection</li>
      <li><svg width="14" height="14" viewBox="0 0 14 14" fill="none" stroke="#333" stroke-width="1.3"><circle cx="7" cy="7" r="6"/><path d="M4 7l2 2 4-4"/></svg>Familial syndromes (including familial adenomatous polyposis)</li>
    </ul>
  </div>
  <ul class="cause-right abs">
    <li><svg class="icon" width="28" height="24" viewBox="0 0 28 24" fill="none" stroke="#0a6ebd" stroke-width="1.5"><path d="M14 3L3 21h22z"/><path d="M9 15h10"/></svg>Eating a diet high in salted, smoked foods and low in fruits and vegetables.</li>
    <li><svg class="icon" width="28" height="24" viewBox="0 0 28 24" fill="none" stroke="#0a6ebd" stroke-width="1.5"><path d="M9 2v8a3 3 0 0 1-3 3v9M5 2v6M9 2v6M19 22V2c3 2 4 6 4 10h-4"/></svg>Eating foods that have not been prepared or stored properly.</li>
    <li><svg class="icon" width="28" height="24" viewBox="0 0 28 24" fill="none" stroke="#0a6ebd" stroke-width="1.5"><circle cx="10" cy="4" r="2.5"/><circle cx="19" cy="4" r="2.5"/><path d="M10 8v14M19 8v14M6 12l4-4 4 4M15 12l4-4 4 4"/></svg>Being older or male.</li>
    <li><svg class="icon" width="28" height="24" viewBox="0 0 28 24" fill="none" stroke="#0a6ebd" stroke-width="1.5"><rect x="3" y="14" width="22" height="5" rx="1"/><path d="M10 11c0-3 3-3 3-6M15 11c0-3 3-3 3-6"/></svg>Smoking cigarettes.</li>
    <li><svg class="icon" width="28" height="24" viewBox="0 0 28 24" fill="none" stroke="#0a6ebd" stroke-width="1.5"><circle cx="9" cy="10" r="6"/><path d="M4 21c2-4 8-4 10 0M18 4c3 2 6 6 6 11"/></svg>Having a mother, father, sister, or brother who has had stomach cancer.</li>
  </ul>
</section>

<section class="symptoms">
  <div class="diagram abs" role="img" aria-label="Medical illustration of stomach wall layers showing tumour stages 0 to 4, and a stomach with a tumour"></div>
  <h2 class="section-title abs">Stomach Cancer Symptoms</h2>
  <div class="symptom-card card-early abs">
    <h3>In the early stages of stomach cancer, the following signs and symptoms may occur:</h3>
    <ul><li>Indigestion and stomach discomfort</li><li>A bloated feeling after eating</li><li>Mild nausea</li><li>Loss of appetite</li><li>Heartburn</li></ul>
  </div>
  <div class="symptom-card card-late abs">
    <h3>In more advanced stages of stomach cancer, the following signs and symptoms may occur:</h3>
    <ul><li>Blood in the stool</li><li>Vomiting</li><li>Weight loss for no known reason</li><li>Stomach pain</li><li>Jaundice (yellowing of eyes and skin)</li><li>Ascites (build-up of fluid in the abdomen)</li><li>Trouble swallowing</li></ul>
  </div>
</section>

<section class="diagnosis">
  <div class="diagnosis-art abs" role="img" aria-label="Blue rendering of the inside of a stomach with a cancer cell"></div>
  <h2 class="section-title abs">Stomach Cancer Diagnosis</h2>
  <p class="diag-lead abs">If you or your doctor suspect you may have stomach cancer, make an appointment with a gastroenterologist, which is a doctor who specializes in the digestive system. During an appointment, they will ask you to provide them with stool and blood samples alongside a thorough physical examination.</p>
  <p class="diag-sub abs">They may also ask for imaging, including an:</p>
  <ul class="diag-list abs">
    <li><svg width="14" height="14" viewBox="0 0 14 14" fill="none" stroke="#fff" stroke-width="1.3"><circle cx="7" cy="7" r="6"/><path d="M4 7l2 2 4-4"/></svg><span>Upper gastrointestinal endoscopy where a doctor inserts a thin, lighted tube (an endoscope) into your mouth, down your esophagus, and into your stomach while you’re sedated or under anesthesia. The endoscope allows your doctor to look at the inner lining of the stomach wall. It can also be used to take a sample (biopsy) of any areas your doctor wants analyzed by a pathologist (a doctor who specializes in diagnosing disease).</span></li>
    <li><svg width="14" height="14" viewBox="0 0 14 14" fill="none" stroke="#fff" stroke-width="1.3"><circle cx="7" cy="7" r="6"/><path d="M4 7l2 2 4-4"/></svg><span>Barium swallow X-rays or upper GI series. In this text you drink a liquid solution containing barium, a silver-white metal that shows up on an X-ray and helps doctors see a clear image of any potential abnormalities.</span></li>
    <li><svg width="14" height="14" viewBox="0 0 14 14" fill="none" stroke="#fff" stroke-width="1.3"><circle cx="7" cy="7" r="6"/><path d="M4 7l2 2 4-4"/></svg><span>CT scan (CAT scan). A CT scan is a procedure that makes a series of detailed pictures of areas inside the body that are then linked to an X-ray machine.</span></li>
  </ul>
  <p class="diag-foot abs">Other tests will likely follow.</p>
</section>

<section class="treatments">
  <div class="care-photo abs" role="img" aria-label="Smiling older patient in a hospital gown supported by a nurse"></div>
  <h2 class="section-title abs">Stomach Cancer Cure and Treatments</h2>
  <div class="treat-copy abs">
    <p>In most cases, stomach cancers are only cured when diagnosed in the early stages. Stomach cancer has a five-year survival rate of 33.3 percent.</p>
    <p>Doctors will use some or all of the following treatments in an attempt to get your stomach cancer into remission including surgery, endoscopic mucosal resection, chemotherapy, radiation therapy, chemoradiation, targeted therapy and immunotherapy. Surgery is a common treatment for stomach cancer. The most common surgeries used include subtotal gastrectomy and total gastrectomy. The following procedures can be preformed if the tumor is blocking the stomach but the cancer cannot be removed by standard surgery: endoluminal stent placement, endoluminal laser therapy and gastrojejunostomy.</p>
    <p>Endoscopic mucosal resection is a procedure that uses an endoscope to remove any precancerous growths or early stage cancer from digestive tract lining without surgery. Radiation therapy targets cancer cells by using high- energy X-rays or radiation beams to keep them from growing. This type of treatment can be customized to each patient depending on the type and stage of the cancer being treated.</p>
    <p>Chemotherapy involves very strong drugs that kill cancerous cells and can prevent them from coming back. Chemoradiation therapy combines chemotherapy and radiation therapy to increase the effects of both.</p>
    <p>Targeted therapy uses drugs or other substances to target and attack cancer cells. Usually, targeted therapies are less harmful than chemotherapy or radiation therapy. Patients have special nutritional needs during esophageal cancer treatments. Immunotherapy is a treatment that uses the patient’s immune system to fight cancer.</p>
  </div>
</section>

<section class="survival">
  <h2 class="section-title abs">Stomach Cancer Survival Rates</h2>
  <div class="surv-copy abs">
    <p>When people measure the survival rates of cancer, they primarily focus on the five-year survival rate. The five-year survival rate measures how many people with a certain type of cancer survived five years or more after diagnosis and the beginning of treatment.</p>
    <p>The Survey of Outcomes and Registry Tracking (SORT) program keeps track of cancer statistics in the United States. They also have a system to judge where cancer is in its growth cycle. There are three categories—localized, regional, and distant.</p>
    <p>Localized refers to cancer that only exists in the area where cancerous growth began. The initial cancerous growth has not spread to any other part of the body. The five-year survival rate for localized stomach cancer is 71.8%.</p>
    <p>Regional refers to cancer that has spread from its original location, but not to places far away. In the case of stomach cancer, this could mean spreading to the esophagus or colon among other locations. The five-year survival rate for regional stomach cancer is 32.9%.</p>
    <p>Distant refers to cancer that has spread to places far from the original location of the cancerous growth. This could mean spreading to the lungs, brain, blood or any other part of your body. The five-year survival rate for distant stomach cancer is 5.9%.</p>
  </div>
  <div class="stat-card stat-local abs">
    <div class="stat-head"><svg width="26" height="24" viewBox="0 0 28 24" fill="none" stroke="#0a6ebd" stroke-width="1.5"><circle cx="9" cy="10" r="6"/><path d="M4 21c2-4 8-4 10 0M18 4c3 2 6 6 6 11"/></svg><span>The five-year survival rate for localized stomach cancer</span></div>
    <div class="stat-value">71.8%</div>
  </div>
  <div class="stat-card stat-regional abs">
    <div class="stat-head"><svg width="26" height="24" viewBox="0 0 28 24" fill="none" stroke="#0a6ebd" stroke-width="1.5"><circle cx="9" cy="10" r="6"/><path d="M4 21c2-4 8-4 10 0M18 4c3 2 6 6 6 11"/></svg><span>The five-year survival rate for regional stomach cancer is</span></div>
    <div class="stat-value" style="margin-left:20px">32.9%.</div>
  </div>
  <div class="stat-card stat-distant abs">
    <div class="stat-head"><svg width="26" height="24" viewBox="0 0 28 24" fill="none" stroke="#0a6ebd" stroke-width="1.5"><circle cx="9" cy="10" r="6"/><path d="M4 21c2-4 8-4 10 0M18 4c3 2 6 6 6 11"/></svg><span>The five-year survival rate for distant stomach cancer</span></div>
    <div class="stat-value" style="margin-top:14px">5.9%</div>
  </div>
</section>

<section class="closing" role="img" aria-label="Dark blue anatomical rendering of a torso with a glowing stomach">
  <p class="abs">Stomach cancer represents almost 1.4 percent of all new cancer cases in the US. Many factors influence the risk of getting stomach cancer. If you believe you are at risk of stomach cancer or exhibit any of the associated symptoms, contact your healthcare provide right away.</p>
</section>

<footer class="site-footer">
  <div class="brand abs"><span class="brand-mark"></span><span class="brand-name">Velsantrum Family Foundation</span></div>
  <div class="foot-contact abs">
    <div><svg width="12" height="12" viewBox="0 0 12 12"><path d="M2.5 1l2 2.5-1.2 1.2a7 7 0 0 0 4 4L8.5 7.5 11 9.5 9.8 11C5 11 1 7 1 2.2z" fill="#222"/></svg>(555) 014-2290</div>
    <div><svg width="12" height="10" viewBox="0 0 16 12" fill="none" stroke="#222" stroke-width="1.6"><rect x="1" y="1" width="14" height="10" rx="1"/><path d="M1 1l7 6 7-6"/></svg>mara@velsantrum.org</div>
  </div>
  <p class="foot-legal abs">The Velsantrum Family Foundation is a designated 501(c)3 © 2020 Velsantrum Family Foundation. All Rights Reserved. Learning Together, Caring Together.</p>
</footer>

</body>
</html>
```